Flooring Billboard Highlighting Large In Stock Inventory

Looking to create a billboard that primarily highlights our logo but also calls out our large in stock inventory and has the city we are located in and phone number at the bottom. Looking for a professional looking design, that is simplistic yet informative.

Location: Brookvale, MN, Near Exit 148

Phone: (715) 381-6094

Website: www.plankhavenstore.example

Products: Carpet, Hardwood, Laminate, Vinyl, Luxury Vinyl Plank & Window Treatments

Callouts:
-Free Estimates
-Wisconsin's In Stock Flooring Store
-Slogan: "Big city selection, small town service"

Target Market(s)

Home buyers, DIY'ers, Remoderls, designers

Industry/Entity Type

Flooring, Construction

Font styles to use
Serif

Requirements
Must have
• My logo, location, phone number and call out our large in stock inventory
Nice to have
• Call out the products we have and our slogan

```html
<!DOCTYPE html>
<html lang="en">
<head>
<meta charset="utf-8">
<title>Plankhaven Billboard</title>
<link rel="stylesheet" href="https://fonts.googleapis.com/css2?family=Nunito:wght@800;900&family=Oswald:wght@500&display=swap">
<style>
  :root {
    --teal: #278b90;
    --rust: #b2530f;
    --white: #ffffff;
    --backdrop: #ebe7e8;
  }
  * { margin: 0; padding: 0; box-sizing: border-box; }
  html, body { width: 1200px; height: 1192px; overflow: hidden; background: var(--backdrop); }
  .billboard {
    position: absolute; left: 40px; top: 420px;
    width: 1120px; height: 352px; background: var(--white);
    font-family: "Nunito", sans-serif; font-weight: 900;
  }
  .billboard-shapes { position: absolute; inset: 0; }
  .brand {
    position: absolute; left: 41px; top: 95px; height: 110px;
    display: flex; align-items: center; gap: 18px;
  }
  .brand-square { width: 78px; height: 78px; background: var(--teal); flex: none; }
  .brand-name { font-size: 74px; color: var(--rust); letter-spacing: -1px; line-height: 1; white-space: nowrap; }
  .slogan {
    position: absolute; left: 548px; top: 8px; width: 560px;
    color: var(--white); font-size: 45px; font-weight: 900; line-height: 57px; text-align: center;
    white-space: nowrap;
  }
  .products {
    position: absolute; right: 33px; top: 141px;
    color: var(--rust); font-size: 24px; font-weight: 800; line-height: 32px; text-align: right;
    white-space: nowrap;
  }
  .offer {
    position: absolute; left: 522px; top: 221px; width: 580px; height: 45px;
    color: var(--white); font-size: 23px; font-weight: 800; line-height: 45px; text-align: center;
    white-space: nowrap;
  }
  .contact {
    position: absolute; top: 282px; height: 70px;
    display: flex; align-items: center; gap: 10px;
    font-family: "Oswald", sans-serif; font-weight: 500; font-size: 31px; color: var(--white);
    white-space: nowrap;
  }
  .contact svg { width: 34px; height: 34px; flex: none; }
  .contact-phone { left: 24px; }
  .contact-web { left: 268px; font-size: 30px; letter-spacing: -0.4px; }
  .contact-location { right: 19px; top: 296px; height: 56px; }
  .contact-location svg { width: 22px; height: 28px; }
</style>
</head>
<body>
  <section class="billboard">
    <svg class="billboard-shapes" viewBox="0 0 1120 352" width="1120" height="352" aria-hidden="true">
      <polygon points="475,0 497,0 552,129 530,129" fill="var(--rust)"/>
      <polygon points="497,0 1120,0 1120,129 552,129" fill="var(--teal)"/>
      <rect x="522" y="221" width="580" height="45" fill="var(--rust)"/>
      <polygon points="0,282 648,282 697,352 0,352" fill="var(--teal)"/>
      <polygon points="672,296 1120,296 1120,352 706,352" fill="var(--rust)"/>
    </svg>

    <div class="brand">
      <span class="brand-square"></span>
      <span class="brand-name">Plankhaven</span>
    </div>

    <h1 class="slogan">BIG CITY SELECTION,<br>SMALL TOWN SERVICE</h1>

    <p class="products">Carpet, Hardwood, Laminate, Vinyl,<br>Luxury Vinyl Plank &amp; Window Treatments</p>

    <p class="offer">Free Estimates and Large In Stock Inventory</p>

    <div class="contact contact-phone">
      <svg viewBox="0 0 32 32" aria-hidden="true">
        <path d="M9 4l4 6-3 3c1.5 3.5 5 7 9 9l3-3 6 4-3 5C14 27 5 18 4 7z" fill="none" stroke="var(--white)" stroke-width="2.6" stroke-linejoin="round"/>
        <path d="M19 5a9 9 0 0 1 8 8M19 10a4 4 0 0 1 3 3" fill="none" stroke="var(--white)" stroke-width="2.4" stroke-linecap="round"/>
      </svg>
      <span>(715) 381-6094</span>
    </div>

    <div class="contact contact-web">
      <svg viewBox="0 0 32 32" aria-hidden="true">
        <circle cx="16" cy="16" r="13" fill="none" stroke="var(--white)" stroke-width="2.6"/>
        <ellipse cx="16" cy="16" rx="5.5" ry="13" fill="none" stroke="var(--white)" stroke-width="2"/>
        <path d="M3 16h26M6 9h20M6 23h20" stroke="var(--white)" stroke-width="2"/>
      </svg>
      <span>www.plankhavenstore.example</span>
    </div>

    <div class="contact contact-location">
      <svg viewBox="0 0 22 28" aria-hidden="true">
        <path d="M11 1a9 9 0 0 0-9 9c0 7 9 17 9 17s9-10 9-17a9 9 0 0 0-9-9z" fill="var(--white)"/>
        <circle cx="11" cy="10" r="3.5" fill="var(--rust)"/>
      </svg>
      <span>Brookvale, MN, Near Exit 148</span>
    </div>
  </section>
</body>
</html>
```